Australian Lipstick Brand

We need packaging design for our tube for lipstick - the brand name is Vela. We are looking for a fun designs on the tube, integrating the logo.
The tube will be a frosted glass, and the lid black.
I will need the designs back in AI format.
I've attached a photo of an example - with our logo, but this is not want we are looking for. We are looking for something fun, but not too kiddy.
Updates
Hi Guys,
I have submitted a few images - the first image is kind of the design I would like something similar too (we are going for a candy theme) will still need the logo integrated.
The second picture is the picture of what the tube should look like. It is a tube (like a lipgloss/ lipstain)
Please email me if you have any further questions.
Thanks,
Marisa
Target Market(s)
Women aged between 16-35

```html
<!DOCTYPE html>
<html lang="en">
<head>
<meta charset="utf-8">
<title>Vela Lipstick – Tube Label</title>
<link href="https://fonts.googleapis.com/css2?family=Josefin+Sans:wght@300;400&display=swap" rel="stylesheet">
<style>
  :root {
    --canvas: #ffffff;
    --berry: #be0058;
    --pattern-pink: #f7a9c9;
    --pattern-coral: #fbc3a6;
    --pattern-light: #fdebf2;
    --ink-light: #ffffff;
  }
  * { margin: 0; padding: 0; box-sizing: border-box; }
  html, body {
    width: 1141px;
    height: 1200px;
    overflow: hidden;
    background: var(--canvas);
    font-family: "Josefin Sans", sans-serif;
  }
  .canvas { position: relative; width: 1141px; height: 1200px; }

  .pattern-fill {
    position: absolute;
    background:
      radial-gradient(circle at 30% 25%, var(--pattern-pink) 0%, transparent 45%),
      radial-gradient(circle at 70% 70%, var(--pattern-coral) 0%, transparent 45%),
      linear-gradient(160deg, var(--pattern-light), var(--pattern-pink) 60%, var(--pattern-light));
  }

  /* Flat label artwork */
  .label-flat .pattern-fill { left: 227px; top: 306px; width: 180px; height: 567px; }
  .label-flat .color-panel {
    position: absolute; left: 407px; top: 306px; width: 178px; height: 567px;
    background: var(--berry);
  }

  .brand-band {
    position: absolute;
    background: var(--berry);
    color: var(--ink-light);
  }
  .brand-name {
    position: absolute;
    white-space: nowrap;
    font-weight: 300;
    transform-origin: left top;
    transform: rotate(-90deg);
    line-height: 1;
  }
  .product-type {
    position: absolute;
    left: 0; right: 0;
    text-align: center;
    font-weight: 300;
  }

  .label-flat .brand-band { left: 282px; top: 306px; width: 76px; height: 265px; }
  .label-flat .brand-name { left: 14px; top: 170px; font-size: 62px; }
  .label-flat .product-type { bottom: 8px; font-size: 20px; }

  /* Tube mock-up */
  .tube-preview .pattern-fill {
    left: 722px; top: 312px; width: 128px; height: 324px;
    border-radius: 10px;
  }
  .tube-preview .brand-band { left: 757px; top: 310px; width: 62px; height: 212px; }
  .tube-preview .brand-name { left: 12px; top: 136px; font-size: 50px; }
  .tube-preview .product-type { bottom: 6px; font-size: 17px; }
</style>
</head>
<body>
<main class="canvas">
  <section class="label-flat">
    <div class="pattern-fill" role="img" aria-label="Doodled hearts and flowers pattern in pink, red and orange on white"></div>
    <div class="color-panel"></div>
    <div class="brand-band">
      <span class="brand-name">Vela</span>
      <span class="product-type">Lipstick</span>
    </div>
  </section>

  <section class="tube-preview">
    <div class="pattern-fill" role="img" aria-label="Tube wrapped in doodled hearts and flowers pattern in pink, red and orange"></div>
    <div class="brand-band">
      <span class="brand-name">Vela</span>
      <span class="product-type">Lipstick</span>
    </div>
  </section>
</main>
</body>
</html>
```